BWR Brochure Design Project

Bluewater Ridge MaintenanceChanges needed to attached flyer...Contact should be Customer Service instead of Dale Perkett.Contact number is 216-555-0187.Cleaning pictures welcome from carpet cleaning, vacuuming floors, mopping, Staff cleaning office environment (not homes). Multi-cultural staff pictures. We currently clean in 18 states around the USA. We DO NOT do screen cleaning or parking lot striping. We do everything else listed in the flyer. The map is incorrect.... we service AR CA CO FL IA IN KY KS LA MA MD MI MN MO NJ OH PA SD TX WV VA.

Address
2400 Linden Ave West
Suite 3200
Cleveland, Ohio 44114

Target Market(s)

Movie Theaters and Entertainment Venues

Industry/Entity Type

Cleaning Service

Requirements
Must have
• A NEW MAP.
• New Pictures

```html
<!DOCTYPE html>
<html lang="en">
<head>
<meta charset="utf-8">
<title>Bluewater Ridge Maintenance – Theatre Cleaning Flyer</title>
<link href="https://fonts.googleapis.com/css2?family=EB+Garamond:wght@400;700&family=Arimo:wght@400;700&family=Oswald:wght@500&display=swap" rel="stylesheet">
<style>
  :root {
    --backdrop: #6b6b6b;
    --ink: #111111;
    --black: #000000;
    --white: #ffffff;
    --green: #8cc47e;
    --green-deep: #5f8f58;
    --ticket: #9fd08f;
    --ticket-ink: #3a4a38;
    --panel: #e4e4e4;
    --text: #1a1a1a;
    --list: #333333;
  }
  * { box-sizing: border-box; margin: 0; padding: 0; }
  html, body { width: 1200px; height: 1169px; overflow: hidden; }
  body { background: var(--backdrop); position: relative; font-family: "Arimo", Arial, sans-serif; color: var(--text); }

  .flyer { position: absolute; left: 233px; top: 100px; width: 704px; height: 939px; background: var(--white); overflow: hidden; }

  .hero { position: absolute; left: 0; top: 0; width: 704px; height: 223px;
    background: radial-gradient(ellipse at 45% 35%, #a6d59a 0%, #86b87b 45%, #6e8f6a 100%); }
  .hero-seats { position: absolute; left: 0; bottom: 0; width: 704px; height: 70px;
    background: linear-gradient(to bottom, rgba(70,20,20,0.35), #141414 85%); }
  .brand { position: absolute; left: 48px; top: 50px; display: flex; align-items: center; gap: 12px; }
  .brand-mark { width: 22px; height: 22px; background: var(--ink); }
  .brand-name { font-family: "EB Garamond", Georgia, serif; font-size: 34px; line-height: 1; color: var(--white); letter-spacing: 0.5px; }

  .call-ticket { position: absolute; left: 471px; top: 56px; width: 196px; height: 91px;
    background: var(--ticket); border: 2px solid var(--green-deep); border-radius: 4px;
    display: flex; flex-direction: column; align-items: center; justify-content: center;
    font-family: "Oswald", "Arial Narrow", sans-serif; font-weight: 500; color: var(--ticket-ink); line-height: 1.1; }
  .call-ticket .call-label { font-size: 32px; letter-spacing: 1px; }
  .call-ticket .call-number { font-size: 20px; letter-spacing: 0.5px; }

  .headline-band { position: absolute; left: 0; top: 223px; width: 704px; height: 153px; background: var(--black); }
  .headline { position: absolute; left: 47px; top: 22px; font-family: "EB Garamond", Georgia, serif; font-weight: 400;
    font-size: 54px; line-height: 62px; color: var(--green); white-space: nowrap; }

  .intro { position: absolute; left: 47px; top: 408px; width: 365px; font-size: 16.5px; line-height: 26px; }
  .intro p { margin-bottom: 14px; }
  .intro .cta { color: var(--green); font-weight: 700; }
  .intro .contact-name { font-weight: 700; margin-bottom: 0; }

  .coverage { position: absolute; left: 450px; top: 376px; width: 254px; height: 516px; background: var(--panel); }
  .coverage-title { position: absolute; left: 32px; top: 45px; font-size: 15px; line-height: 20px; font-weight: 700; letter-spacing: 0.5px; color: var(--ink); }
  .state-list { position: absolute; top: 99px; list-style: none; font-size: 12.3px; line-height: 20.2px; color: var(--list); }
  .state-list.col-a { left: 32px; }
  .state-list.col-b { left: 133px; }
  .coverage-map { position: absolute; left: 21px; top: 326px; width: 222px; height: 140px;
    background: linear-gradient(135deg, #c4c4c4 0%, #9fcf92 55%, #c4c4c4 100%); border-radius: 18px 30px 12px 40px; }
  .coming-soon { position: absolute; left: 0; top: 472px; width: 254px; text-align: center; font-family: "EB Garamond", Georgia, serif;
    font-weight: 700; font-size: 16px; line-height: 18px; color: var(--green); }

  .footer { position: absolute; left: 0; top: 892px; width: 704px; height: 47px; background: var(--black);
    color: var(--white); font-size: 11.5px; display: flex; align-items: center; padding-left: 47px; gap: 6px; white-space: nowrap; }
  .footer .footer-brand { color: var(--green); }
</style>
</head>
<body>
  <main class="flyer">
    <header class="hero" role="img" aria-label="Photo of rows of red theatre seats under a green spotlight glow">
      <div class="hero-seats"></div>
    </header>
    <div class="brand">
      <span class="brand-mark"></span>
      <span class="brand-name">BLUEWATER RIDGE</span>
    </div>
    <div class="call-ticket">
      <span class="call-label">CALL US!</span>
      <span class="call-number">216-555-0187</span>
    </div>

    <section class="headline-band">
      <h1 class="headline">Experts in Cleaning Theatres<br>and Entertainment Venues</h1>
    </section>

    <section class="intro">
      <p>At Bluewater Ridge, we treat each building with special care. Our job is to concentrate on the cleanliness of your building, lessening your workload and allowing you to concentrate on the many demands of running your business.</p>
      <p>We provide expert cleaning services seven days a week, 365 days a year. When you leave your facility each night, we give you peace of mind that your assets will be cared for and cleaned to the highest professional standards.</p>
      <p class="cta">For more information or to obtain a free quote, please contact:</p>
      <p class="contact-name">Customer Service</p>
      <p class="contact-phone">216-555-0187</p>
    </section>

    <aside class="coverage">
      <h2 class="coverage-title">WE CURRENTLY<br>SERVE THEATRES IN:</h2>
      <ul class="state-list col-a">
        <li>Arkansas</li><li>California</li><li>Colorado</li><li>Florida</li><li>Indiana</li><li>Iowa</li><li>Kansas</li><li>Kentucky</li><li>Louisiana</li><li>Maryland</li><li>Massachusetts</li>
      </ul>
      <ul class="state-list col-b">
        <li>Michigan</li><li>Minnesota</li><li>Missouri</li><li>New Jersey</li><li>Ohio</li><li>Pennsylvania</li><li>South Dakota</li><li>Texas</li><li>Virginia</li><li>West Virginia</li>
      </ul>
      <div class="coverage-map" role="img" aria-label="Map of the United States with served states highlighted in green"></div>
      <p class="coming-soon">COMING TO<br>YOUR STATE SOON!</p>
    </aside>

    <footer class="footer">
      <span class="footer-brand">Bluewater Ridge Maintenance</span>
      <span>|</span><span>2400 Linden Avenue West Suite 3200</span>
      <span>|</span><span>Cleveland, OH 44114</span>
      <span>|</span><span>216-555-0187</span>
    </footer>
  </main>
</body>
</html>
```